carpet cleaning flyer/leaflet modern/upmarket twist

We are Brightwell Fresh, We do carpet & upholstery cleaning for the domestic market, if you are able to incorporate images like the ones I have provided that would be awesome, please feel free to find similar! mine are only examples. id like a front cover photo with the company name running through it, and the back to be half picture and then the detailing of what we do which is in the document I've uploaded
Target Market(s)
Domestic house hold
Industry/Entity Type
Cleaning Service
Colors
eea4c8
e667a6
c3c3c3
cbcbcb
aaaaaa
f59296
Requirements
Must have
- It must be 2 sided also have A modern but upmarket feel, a luxury. a front picture with name on it, back page with picture and writing from the word document.
Nice to have
- a input from yourselves, your twist on it

```html
<!DOCTYPE html>
<html lang="en">
<head>
<meta charset="utf-8">
<title>Brightwell Fresh – Carpet &amp; Upholstery Cleaning</title>
<link href="https://fonts.googleapis.com/css2?family=Archivo+Black&family=Lato:wght@400;700&family=Oswald:wght@600&display=swap" rel="stylesheet">
<style>
  :root{
    --pink:#e667a6;
    --pink-bright:#f04fd0;
    --pink-soft:#eea4c8;
    --grey-light:#cbcbcb;
    --grey-mid:#c3c3c3;
    --grey-dark:#aaaaaa;
    --ink:#1d1d1d;
    --white:#ffffff;
  }
  html,body{margin:0;padding:0;overflow:hidden;background:var(--white);}
  .flyer{
    position:relative;width:853px;height:1200px;overflow:hidden;
    background:var(--white);font-family:"Lato",Arial,sans-serif;color:var(--ink);
  }
  .hero{position:absolute;left:0;top:0;width:853px;height:640px;display:block;}
  .features{
    position:absolute;left:37px;top:650px;width:779px;margin:0;
    display:grid;grid-template-columns:144px 1fr;row-gap:0;
    font-size:19.5px;line-height:29px;
  }
  .features dt{
    color:var(--pink-bright);font-weight:700;text-decoration:underline;
  }
  .features dd{margin:0;text-align:justify;}
  .divider{
    position:absolute;left:37px;top:964px;width:779px;height:3px;
    background:var(--pink-bright);
  }
  .brand-name{
    position:absolute;right:37px;top:972px;margin:0;
    font-family:"Archivo Black",Arial,sans-serif;font-weight:400;
    font-size:56px;line-height:68px;color:var(--pink-bright);letter-spacing:0.5px;
  }
  .contact-bar{
    position:absolute;right:37px;display:flex;align-items:center;justify-content:center;
    font-family:"Oswald",Arial,sans-serif;font-weight:600;color:var(--white);
    background:linear-gradient(90deg,rgba(240,79,208,0) 0%,var(--pink-bright) 14%,var(--pink-bright) 100%);
  }
  .contact-bar--phone{top:1044px;width:470px;height:52px;font-size:33px;gap:10px;}
  .contact-bar--email{top:1109px;width:540px;height:54px;font-size:31px;}
  .phone-icon{width:30px;height:30px;}
</style>
</head>
<body>
<main class="flyer">
  <svg class="hero" viewBox="0 0 853 640" xmlns="http://www.w3.org/2000/svg">
    <defs>
      <linearGradient id="stoneTone" x1="0" y1="0" x2="1" y2="1">
        <stop offset="0" stop-color="#bdbdbd"/>
        <stop offset="0.5" stop-color="#d4d4d4"/>
        <stop offset="1" stop-color="#b8b8b8"/>
      </linearGradient>
      <linearGradient id="roomTone" x1="0" y1="0" x2="0" y2="1">
        <stop offset="0" stop-color="#8f9a86"/>
        <stop offset="0.45" stop-color="#a4a8a4"/>
        <stop offset="1" stop-color="#6f7275"/>
      </linearGradient>
    </defs>
    <path role="img" aria-label="Soft grey stone texture backdrop" fill="url(#stoneTone)"
      d="M0 0H853V60C760 40 640 40 520 90C470 112 440 170 380 160C260 140 120 60 0 80Z"/>
    <path fill="var(--grey-mid)" d="M0 40C130 20 260 130 400 150C500 165 560 60 853 45V60C640 50 540 180 420 178C260 175 130 60 0 80Z"/>
    <path fill="none" stroke="var(--pink-bright)" stroke-width="5"
      d="M0 88C140 70 280 170 430 168C560 166 660 70 853 74"/>
    <path role="img" aria-label="Photo of a living room with a grey armchair, pouffe and carpet by a window"
      fill="url(#roomTone)"
      d="M0 100C150 84 280 180 430 178C560 176 670 84 853 86V462C720 430 600 470 470 530C400 562 330 590 260 585C160 578 80 470 0 468Z"/>
    <path fill="var(--pink-bright)"
      d="M0 468C80 470 160 578 260 585C330 590 400 562 470 530C600 470 720 430 853 462V474C720 450 600 500 470 570C400 606 330 625 250 612C150 598 80 490 0 480Z"/>
  </svg>

  <dl class="features">
    <dt>Reliable:</dt>
    <dd>We pride ourselves on providing outstanding services to our customers. From a single carpet or rug, to a whole house clean, we provide a reliable and friendly service. Call us to discuss your needs.</dd>
    <dt>Professional:</dt>
    <dd>Professional: We use the latest hot water extraction cleaning technology to give us the ability to get into the ground down dirt deep down inside the Fibres.</dd>
    <dt>Trustworthy:</dt>
    <dd>We are fully insured to work in your home, we guarantee all our work so if any issues do arise we will do our up most to put it back right for you.</dd>
  </dl>

  <div class="divider"></div>
  <h1 class="brand-name">Brightwell Fresh</h1>

  <div class="contact-bar contact-bar--phone">
    <svg class="phone-icon" viewBox="0 0 24 24" aria-hidden="true">
      <path fill="#ffffff" d="M3 9c0-3 4-5 9-5s9 2 9 5l-3 2-2-2V7.5c-1.3-.4-2.6-.5-4-.5s-2.7.1-4 .5V9l-2 2z"/>
      <path fill="#ffffff" d="M7 11.5 9 9h6l2 2.5V19H7z"/>
      <circle cx="12" cy="14.5" r="2" fill="#f04fd0"/>
    </svg>
    <span>Tel: 01632 960 418</span>
  </div>
  <div class="contact-bar contact-bar--email">Email: sam.hale@brightwellfresh.co.uk</div>
</main>
</body>
</html>
```